Harwell Lawyers Banner

I would like to have a graphic design created for a company banner. The company is Harwell Lawyers and the website is https://harwelllawyers-example.com.au/ We would like a professional banner we are able to put up at events to advertise the company.
The banner size is 800mm wide by 2000mm high so please keep the design inside these constraints.

```html
<!DOCTYPE html>
<html lang="en">
<head>
<meta charset="UTF-8">
<title>Harwell Lawyers – Event Banner</title>
<link href="https://fonts.googleapis.com/css2?family=Montserrat:wght@300;600;700;800&display=swap" rel="stylesheet">
<style>
  :root {
    --page-bg: #dedede;
    --white: #ffffff;
    --ink: #23272b;
    --brand-blue: #2a9bd0;
    --deep-blue: #0f4c6c;
    --gold: #f5b617;
    --gold-dark: #9a6f0c;
    --charcoal: #2b2f33;
  }
  * { margin: 0; padding: 0; box-sizing: border-box; }
  html, body {
    width: 800px; height: 1200px; overflow: hidden;
    background: var(--page-bg);
    font-family: "Montserrat", sans-serif;
  }
  .banner-stage {
    position: absolute; left: 203px; top: 30px;
    width: 393px; height: 1140px;
    box-shadow: 0 6px 18px rgba(0,0,0,0.18);
  }
  .banner {
    position: absolute; left: 0; top: 0;
    width: 464px; height: 1347px;
    transform: scale(0.8463);
    transform-origin: 0 0;
    background: var(--white);
    overflow: hidden;
  }
  .banner-art { position: absolute; inset: 0; }
  .brand-name {
    position: absolute; left: 0; right: 0; top: 62px;
    text-align: center;
    font-weight: 300; font-size: 46px; letter-spacing: 1px;
    color: var(--ink);
  }
  .headline {
    position: absolute; left: 0; right: 0; top: 705px;
    text-align: center; color: var(--white);
    font-weight: 800; line-height: 1;
  }
  .headline .line-one { display: block; font-size: 60px; letter-spacing: -0.5px; }
  .headline .line-two { display: block; font-size: 75px; margin-top: 4px; letter-spacing: -1px; }
  .intro {
    position: absolute; left: 40px; right: 40px; top: 899px;
    text-align: center; color: var(--white);
    font-weight: 700; font-size: 20.5px; line-height: 25px;
  }
  .ribbon-title {
    position: absolute; left: 0; right: 0; top: 1006px;
    text-align: center; color: var(--ink);
    font-weight: 800; font-size: 21px; letter-spacing: 1px;
  }
  .services {
    position: absolute; top: 1058px; list-style: none;
    color: var(--white); font-weight: 600; font-size: 13.5px; line-height: 16px;
    letter-spacing: 0.3px;
  }
  .services.col-left { left: 62px; width: 175px; }
  .services.col-right { left: 253px; width: 170px; }
  .services li { position: absolute; left: 0; padding-left: 22px; }
  .services li svg { position: absolute; left: 0; top: 1px; width: 13px; height: 13px; }
  .web-address {
    position: absolute; left: 0; right: 0; top: 1281px;
    text-align: center; color: var(--white);
    font-weight: 600; font-size: 17px; letter-spacing: 1.6px;
  }
</style>
</head>
<body>
<div class="banner-stage">
  <div class="banner">
    <svg class="banner-art" width="464" height="1347" viewBox="0 0 464 1347">
      <defs>
        <linearGradient id="blueFade" x1="0" y1="0" x2="0" y2="1">
          <stop offset="0" stop-color="var(--brand-blue)"/>
          <stop offset="1" stop-color="var(--deep-blue)"/>
        </linearGradient>
        <linearGradient id="photoTone" x1="0" y1="0" x2="0" y2="1">
          <stop offset="0" stop-color="#d7e2ec"/>
          <stop offset="0.35" stop-color="#8ea2b6"/>
          <stop offset="0.7" stop-color="#2a3845"/>
          <stop offset="1" stop-color="#3b2c20"/>
        </linearGradient>
      </defs>

      <polygon class="blue-panel" points="0,687 464,452 464,1347 0,1347" fill="url(#blueFade)"/>
      <polygon class="accent-stripe" points="0,652 62,624 84,660 0,690" fill="var(--charcoal)"/>

      <polygon class="frame-left" points="24,410 24,207 64,167 223,167 223,190 72,190 53,209 53,410" fill="var(--gold)"/>
      <path class="frame-right" d="M238,170 L408,170 L435,199 L435,413" fill="none" stroke="var(--gold)" stroke-width="7"/>
      <polygon class="frame-bottom" points="438,430 438,640 403,675 238,675 238,652 392,652 410,634 410,430" fill="var(--gold)"/>

      <g role="img" aria-label="Photo of glass office towers seen from below against a pale sky">
        <polygon points="53,209 72,190 392,190 410,209 410,634 392,652 72,652 53,634" fill="url(#photoTone)"/>
      </g>

      <line x1="45" y1="873" x2="418" y2="873" stroke="#5aa9cf" stroke-width="1" opacity="0.6"/>
      <rect x="183" y="869" width="93" height="8" rx="4" fill="var(--gold)"/>

      <path d="M19,963 L50,963 L50,936" fill="none" stroke="var(--white)" stroke-width="2"/>
      <path d="M51,1000 L51,972 L81,972" fill="none" stroke="var(--white)" stroke-width="5"/>

      <rect x="35" y="1020" width="394" height="237" fill="none" stroke="var(--white)" stroke-width="1.5"/>
      <path d="M385,1240 L405,1240 L405,1220" fill="none" stroke="var(--white)" stroke-width="2"/>
      <path d="M410,1257 L410,1238 L429,1238" fill="none" stroke="var(--white)" stroke-width="4"/>

      <polygon points="80,1000 108,1000 108,1022" fill="var(--gold-dark)"/>
      <polygon points="385,1000 357,1000 357,1022" fill="var(--gold-dark)"/>
      <path d="M100,1000 L365,1000 Q360,1040 335,1042 L130,1042 Q105,1040 100,1000 Z" fill="var(--gold)"/>
    </svg>

    <div class="brand-name">Harwell Lawyers</div>

    <h1 class="headline">
      <span class="line-one">COMMERCIAL</span>
      <span class="line-two">LAW FIRM</span>
    </h1>

    <p class="intro">Harwell Lawyers is a leading commercial law firm located in Marlow Heights</p>

    <div class="ribbon-title">SPECIALISING IN</div>

    <ul class="services col-left">
      <li style="top:0"><svg viewBox="0 0 14 14"><circle cx="7" cy="7" r="7" fill="#f5b617"/><path d="M3.8,7.2 L6,9.3 L10.2,4.9" fill="none" stroke="#fff" stroke-width="1.8"/></svg>Advising Family<br>Businesses</li>
      <li style="top:48px"><svg viewBox="0 0 14 14"><circle cx="7" cy="7" r="7" fill="#f5b617"/><path d="M3.8,7.2 L6,9.3 L10.2,4.9" fill="none" stroke="#fff" stroke-width="1.8"/></svg>Estate Planning,<br>Administration and<br>Disputes</li>
      <li style="top:112px"><svg viewBox="0 0 14 14"><circle cx="7" cy="7" r="7" fill="#f5b617"/><path d="M3.8,7.2 L6,9.3 L10.2,4.9" fill="none" stroke="#fff" stroke-width="1.8"/></svg>Tax and Structuring</li>
      <li style="top:144px"><svg viewBox="0 0 14 14"><circle cx="7" cy="7" r="7" fill="#f5b617"/><path d="M3.8,7.2 L6,9.3 L10.2,4.9" fill="none" stroke="#fff" stroke-width="1.8"/></svg>Planning and<br>Environment</li>
    </ul>

    <ul class="services col-right">
      <li style="top:0"><svg viewBox="0 0 14 14"><circle cx="7" cy="7" r="7" fill="#f5b617"/><path d="M3.8,7.2 L6,9.3 L10.2,4.9" fill="none" stroke="#fff" stroke-width="1.8"/></svg>Not for Profit and<br>Social Enterprise</li>
      <li style="top:48px"><svg viewBox="0 0 14 14"><circle cx="7" cy="7" r="7" fill="#f5b617"/><path d="M3.8,7.2 L6,9.3 L10.2,4.9" fill="none" stroke="#fff" stroke-width="1.8"/></svg>Management<br>Rights, Property<br>and Developments</li>
      <li style="top:112px"><svg viewBox="0 0 14 14"><circle cx="7" cy="7" r="7" fill="#f5b617"/><path d="M3.8,7.2 L6,9.3 L10.2,4.9" fill="none" stroke="#fff" stroke-width="1.8"/></svg>Litigation and<br>Dispute<br>Resolution</li>
    </ul>

    <div class="web-address">www.harwelllawyers-example.com.au</div>
  </div>
</div>
</body>
</html>
```